Law firm website marketed direct to many individual clients

I need someone to design a very basic website for a law firm that will be very eye catching. It's going to be a single-paged, scrolling website with a small number of folds. I have uploaded a simple word document that outlines the basics of what I thought could be the layout, but I am open to suggestion on font, size, shades of color, organization, etc. etc. Essentially the website just needs to be a very efficient and visually appealing way of conveying some simple messages.

Target Market(s)

High volumes of individuals who have gotten into a car accident and then google on their phones a lawyer to hire to represent them.

Industry/Entity Type

Legal

Number of Pages Required

1 page

Font styles to use
Serif
Sans Serif

Colors
34a7d7
85cae6
0592cd

Requirements
Must have
• Must be bright and grab the users attention with color scheme and layout. The different sections should be done in such a way that they can fit entirely onto one smart phone or tablet screen.
Nice to have
• I'd like to try and see what it looks like if in the middle somewhere there is a fold that says "MEET YOUR ATTORNEYS" and includes individual photos of two attorneys, one on the left side and one on the right. And then a small bio section on them. I don't want the photos to include a square or rectangle background, I want the person in the photo to be superimposed on top of whatever pattern or background you have in the fold.
Should not have
• Do not want too much text. Anything more than 2 sentences in any single place is unacceptable.

```html
<!DOCTYPE html>
<html lang="en">
<head>
<meta charset="utf-8">
<title>Meridian Law Group</title>
<link rel="stylesheet" href="https://fonts.googleapis.com/css2?family=Noto+Serif:wght@400&family=Open+Sans:wght@400;700&family=Roboto+Condensed:wght@400;700&display=swap">
<style>
:root{
  --navy:#14166a;
  --ink:#333;
  --muted:#666;
  --band-grey:#e8e8e8;
  --footer:#3a3a3a;
  --white:#fff;
}
*{box-sizing:border-box;margin:0;padding:0}
html,body{width:1200px;height:2290px;overflow:hidden;background:var(--white)}
body{position:relative;font-family:"Open Sans",sans-serif;color:var(--ink)}
section,header,footer{position:absolute;left:0;width:1200px}

/* header */
.site-header{top:0;height:137px}
.brand{position:absolute;left:83px;top:48px;width:310px;font-family:"Noto Serif",serif;font-size:30px;line-height:40px;color:var(--navy);white-space:nowrap}
.header-call{position:absolute;right:80px;top:26px;display:flex;align-items:center}
.header-call svg{width:34px;height:34px;margin-right:14px}
.header-call .divider{width:1px;height:58px;background:#ccc;margin-right:14px}
.header-call .label{font-size:20px;color:#888;line-height:1.2}
.header-call .number{font-family:"Roboto Condensed",sans-serif;font-weight:700;font-size:30px;color:#333;line-height:1.1}

/* hero */
.hero{top:137px;height:521px;background:linear-gradient(100deg,#8e8a84 0%,#d9d5cf 35%,#f2ede6 65%,#efe3cf 100%)}
.hero-title{position:absolute;right:77px;top:140px;text-align:right;font-family:"Noto Serif",serif;font-weight:400;font-size:48px;line-height:72px;color:var(--navy)}

/* call band */
.call-band{top:658px;height:155px;display:flex}
.call-band .pitch{width:600px;background:var(--band-grey);padding:34px 0 0 80px}
.call-band .pitch small{display:block;font-family:"Noto Serif",serif;font-size:24px;color:#333}
.call-band .pitch strong{display:block;font-family:"Noto Serif",serif;font-weight:400;font-size:36px;color:var(--navy);margin-top:8px}
.call-band .dial{width:600px;background:var(--navy);display:flex;align-items:center;padding-left:35px;color:var(--white)}
.call-word{font-family:"Noto Serif",serif;font-size:40px}
.call-icon{width:64px;height:64px;margin:0 15px}
.call-number{font-weight:700;font-size:42px}

/* features */
.features{top:813px;height:488px}
.feature{position:absolute;top:65px;width:250px;text-align:center}
.feature .ring{width:126px;height:126px;border:2px solid var(--navy);border-radius:50%;margin:0 auto;display:flex;align-items:center;justify-content:center}
.feature .ring svg{width:60px;height:60px}
.feature h3{font-family:"Roboto Condensed",sans-serif;font-weight:400;font-size:24px;line-height:36px;color:#222;margin-top:24px}
.feature p{font-size:15px;line-height:24px;color:var(--muted);margin:4px auto 0;width:228px}
.features .dial{position:absolute;top:350px;left:0;width:1200px;display:flex;justify-content:center;align-items:center}
.features .call-word{color:#333}
.features .call-number{color:var(--navy)}

/* promise */
.promise{top:1301px;height:310px;background:linear-gradient(90deg,#1a1b5c 0%,#242670 55%,#3a3a78 80%,#2a2b68 100%);text-align:center;color:var(--white)}
.promise h2{font-family:"Roboto Condensed",sans-serif;font-weight:400;font-size:52px;margin-top:74px}
.promise p{font-size:20px;line-height:36px;width:620px;margin:14px auto 0}

/* questions */
.questions{top:1611px;height:470px;background:linear-gradient(90deg,#dcdcdc 0%,#eeeeee 40%,#f4f4f4 60%,#dedede 100%);text-align:center}
.questions h2{font-family:"Roboto Condensed",sans-serif;font-weight:400;font-size:52px;color:#333;margin-top:58px}
.questions p{font-size:20px;line-height:37px;color:#555;width:800px;margin:18px auto 0}
.pill{position:absolute;left:339px;top:282px;width:521px;height:89px;border-radius:45px;background:var(--navy);display:flex;align-items:center;justify-content:center;color:var(--white)}
.pill .call-word{font-size:36px}
.pill .call-icon{width:58px;height:58px}
.pill .call-number{font-size:36px}

/* footer */
.site-footer{top:2081px;height:209px;background:var(--footer);color:var(--white)}
.site-footer .brand{color:var(--white);top:46px}
.foot-col{position:absolute;top:52px;text-align:center}
.foot-col h4{font-family:"Noto Serif",serif;font-weight:400;font-size:23px}
.foot-col span{display:flex;align-items:center;justify-content:center;font-size:16px;margin-top:16px}
.foot-col svg{width:18px;height:18px;margin-right:8px}
.site-footer hr{position:absolute;left:77px;top:157px;width:1048px;border:0;border-top:1px solid #5a5a5a}
.copyright{position:absolute;top:172px;width:1200px;text-align:center;font-size:15px}
</style>
</head>
<body>

<header class="site-header">
  <div class="brand">Meridian Law Group</div>
  <div class="header-call">
    <svg viewBox="0 0 24 24" fill="#14166a"><path d="M6.6 10.8c1.4 2.8 3.8 5.1 6.6 6.6l2.2-2.2c.3-.3.7-.4 1-.2 1.1.4 2.3.6 3.6.6.6 0 1 .4 1 1V20c0 .6-.4 1-1 1C10.6 21 3 13.4 3 4c0-.6.4-1 1-1h3.5c.6 0 1 .4 1 1 0 1.3.2 2.5.6 3.6.1.3 0 .7-.2 1l-2.3 2.2z"/></svg>
    <div class="divider"></div>
    <div>
      <div class="label">CALL US NOW</div>
      <div class="number">504-555-0142</div>
    </div>
  </div>
</header>

<section class="hero" role="img" aria-label="Photo of a statue of Lady Justice holding scales in front of marble columns">
  <h1 class="hero-title">WE ARE DEDICATED &amp;<br>EXPERIENCED TRIAL<br>ATTORNEYS.</h1>
</section>

<section class="call-band">
  <div class="pitch">
    <small>ACCIDENT? INJURED?</small>
    <strong>YOUR CASE YOUR MONEY</strong>
  </div>
  <div class="dial">
    <span class="call-word">CALL</span>
    <svg class="call-icon" viewBox="0 0 64 64"><circle cx="32" cy="32" r="30" fill="none" stroke="#fff" stroke-width="2"/><path transform="translate(18 18) scale(1.15)" fill="#fff" d="M6.6 10.8c1.4 2.8 3.8 5.1 6.6 6.6l2.2-2.2c.3-.3.7-.4 1-.2 1.1.4 2.3.6 3.6.6.6 0 1 .4 1 1V20c0 .6-.4 1-1 1C10.6 21 3 13.4 3 4c0-.6.4-1 1-1h3.5c.6 0 1 .4 1 1 0 1.3.2 2.5.6 3.6.1.3 0 .7-.2 1l-2.3 2.2z"/></svg>
    <span class="call-number">504-555-0142</span>
  </div>
</section>

<section class="features">
  <div class="feature" style="left:64px">
    <div class="ring"><svg viewBox="0 0 60 60"><g transform="rotate(-12 30 30)"><rect x="4" y="16" width="52" height="28" rx="2" fill="#14166a"/><circle cx="30" cy="30" r="9" fill="#fff"/><text x="30" y="35" text-anchor="middle" font-family="Open Sans,sans-serif" font-weight="700" font-size="13" fill="#14166a">$</text></g></svg></div>
    <h3>LOW FEES</h3>
    <p>We charge less, so you keep<br>more.</p>
  </div>
  <div class="feature" style="left:336px">
    <div class="ring"><svg viewBox="0 0 60 60" fill="#14166a"><circle cx="16" cy="12" r="5"/><circle cx="30" cy="12" r="5"/><circle cx="44" cy="12" r="5"/><rect x="10" y="19" width="12" height="14" rx="2"/><rect x="24" y="19" width="12" height="14" rx="2"/><rect x="38" y="19" width="12" height="14" rx="2"/><rect x="6" y="32" width="48" height="5"/><rect x="12" y="37" width="4" height="17"/><rect x="28" y="37" width="4" height="17"/><rect x="44" y="37" width="4" height="17"/></svg></div>
    <h3>FREE CONSULTATION</h3>
    <p>It's always free to talk to us.</p>
  </div>
  <div class="feature" style="left:608px">
    <div class="ring"><svg viewBox="0 0 60 60" fill="#14166a"><path transform="translate(8 10) scale(1.7)" d="M6.6 10.8c1.4 2.8 3.8 5.1 6.6 6.6l2.2-2.2c.3-.3.7-.4 1-.2 1.1.4 2.3.6 3.6.6.6 0 1 .4 1 1V20c0 .6-.4 1-1 1C10.6 21 3 13.4 3 4c0-.6.4-1 1-1h3.5c.6 0 1 .4 1 1 0 1.3.2 2.5.6 3.6.1.3 0 .7-.2 1l-2.3 2.2z"/><path d="M34 8a18 18 0 0 1 18 18" fill="none" stroke="#14166a" stroke-width="3"/><path d="M34 15a11 11 0 0 1 11 11" fill="none" stroke="#14166a" stroke-width="3"/></svg></div>
    <h3>GET STARTED USING<br>ONLY YOUR PHONE</h3>
    <p>No need to come to the office,<br>sign up using your phone.</p>
  </div>
  <div class="feature" style="left:878px">
    <div class="ring"><svg viewBox="0 0 60 60" fill="#14166a"><circle cx="30" cy="19" r="11"/><path d="M10 54c0-13 9-20 20-20s20 7 20 20z"/></svg></div>
    <h3>SPEAK DIRECTLY TO<br>A LAWYER</h3>
    <p>No staff screening. Talk right to<br>a lawyer on your first call.</p>
  </div>
  <div class="dial">
    <span class="call-word">CALL</span>
    <svg class="call-icon" viewBox="0 0 64 64"><circle cx="32" cy="32" r="30" fill="none" stroke="#333" stroke-width="2"/><path transform="translate(18 18) scale(1.15)" fill="#333" d="M6.6 10.8c1.4 2.8 3.8 5.1 6.6 6.6l2.2-2.2c.3-.3.7-.4 1-.2 1.1.4 2.3.6 3.6.6.6 0 1 .4 1 1V20c0 .6-.4 1-1 1C10.6 21 3 13.4 3 4c0-.6.4-1 1-1h3.5c.6 0 1 .4 1 1 0 1.3.2 2.5.6 3.6.1.3 0 .7-.2 1l-2.3 2.2z"/></svg>
    <span class="call-number">504-555-0142</span>
  </div>
</section>

<section class="promise" role="img" aria-label="Navy-tinted photo of a judge's gavel over a desk">
  <h2>NO FEE UNLESS WE WIN</h2>
  <p>We don't get paid unless you get paid. It's as simple as that. We let our results do the talking for us.</p>
</section>

<section class="questions" role="img" aria-label="Faded photo of attorneys meeting with a client at a desk">
  <h2>QUESTIONS ABOUT ANYTHING?</h2>
  <p>We're here to help. Feel free to call us at 504-555-0142 to speak to one of our attorneys. With extensive experience in helping clients get the results that they want, our team is always just a phone call away.</p>
  <div class="pill">
    <span class="call-word">CALL</span>
    <svg class="call-icon" viewBox="0 0 64 64"><circle cx="32" cy="32" r="30" fill="none" stroke="#fff" stroke-width="2"/><path transform="translate(18 18) scale(1.15)" fill="#fff" d="M6.6 10.8c1.4 2.8 3.8 5.1 6.6 6.6l2.2-2.2c.3-.3.7-.4 1-.2 1.1.4 2.3.6 3.6.6.6 0 1 .4 1 1V20c0 .6-.4 1-1 1C10.6 21 3 13.4 3 4c0-.6.4-1 1-1h3.5c.6 0 1 .4 1 1 0 1.3.2 2.5.6 3.6.1.3 0 .7-.2 1l-2.3 2.2z"/></svg>
    <span class="call-number">504-555-0142</span>
  </div>
</section>

<footer class="site-footer">
  <div class="brand">Meridian Law Group</div>
  <div class="foot-col" style="left:430px;width:345px">
    <h4>Crummy Office Somewhere</h4>
    <span><svg viewBox="0 0 24 24" fill="#fff"><path d="M12 2a7 7 0 0 0-7 7c0 5 7 13 7 13s7-8 7-13a7 7 0 0 0-7-7zm0 9.5A2.5 2.5 0 1 1 12 6.5a2.5 2.5 0 0 1 0 5z"/></svg>Harbor City, LA 70000</span>
  </div>
  <div class="foot-col" style="left:870px;width:200px">
    <h4>Contact No.</h4>
    <span><svg viewBox="0 0 24 24" fill="#fff"><path d="M6.6 10.8c1.4 2.8 3.8 5.1 6.6 6.6l2.2-2.2c.3-.3.7-.4 1-.2 1.1.4 2.3.6 3.6.6.6 0 1 .4 1 1V20c0 .6-.4 1-1 1C10.6 21 3 13.4 3 4c0-.6.4-1 1-1h3.5c.6 0 1 .4 1 1 0 1.3.2 2.5.6 3.6.1.3 0 .7-.2 1l-2.3 2.2z"/></svg>504-555-0142</span>
  </div>
  <hr>
  <div class="copyright">© <b>Meridian Law Group</b> - 2016. All Rights Reserved.</div>
</footer>

</body>
</html>
```